Shopify Design for wedding invitations

We are a greeting card manufactory, special in wedding invitation
I need a shopify website for our wedding invitation brand. (Lovmira), atttach you can find our logo.
We are looking for someone to create a modern and clean looking e-commerce store for our wedding invitation through Shopify. We need some life, professionalism and style put into our site. We will have a variety serie of products : laser cut wedding invitation, popup wedding invitaiton, vintage wedding invitation, handmade wedding invitation, printing invitation, Custom wedding cards, wedding stationery (including favor box, table card, place card, escort card, number card), Thank you card. our online store requires easy navigation to categories divided by product type.

our market is , Eourpe and USA,
please choose a good color for it.
you can go to our website: www.bluestonecraft.com and check our product.
also you can go to Vendoro 4 new items.
https://www.vendoro-shop.com/dp/X47K8Q2M19?ref=abc_item_dp

Target Market(s)

Europe and USA

Industry/Entity Type

wedding

Number of Pages Required

1 page

Requirements
Must have
• Logo, 3 banners than can be changed each 3-5 seconds.
Nice to have
• nice icon and font, beautiful color,

```html
<!DOCTYPE html>
<html lang="en">
<head>
<meta charset="utf-8">
<title>Lovmira – Wedding Invitations</title>
<link href="https://fonts.googleapis.com/css2?family=Lato:wght@400;700;900&family=Sofia&display=swap" rel="stylesheet">
<style>
:root{
  --green:#6c9a32;
  --green-dark:#5d8a28;
  --ink:#111;
  --text:#555;
  --muted:#777;
  --bar:#1a1a1a;
  --white:#fff;
  --wood:#6b3a22;
}
*{box-sizing:border-box;margin:0;padding:0}
html,body{width:1200px;height:2883px;overflow:hidden;background:var(--white);font-family:'Lato',sans-serif;color:var(--text)}
.page{position:relative;width:1200px;height:2883px}
.abs{position:absolute}
.topbar{top:0;left:0;width:1200px;height:30px;font-size:14px;font-weight:700;color:var(--ink)}
.topbar .links{position:absolute;right:130px;top:6px}
.topbar .cart{position:absolute;right:122px;top:4px}
.navbar{top:30px;left:0;width:1200px;height:72px;background:var(--bar)}
.logo{position:absolute;left:125px;top:20px;font-family:'Lato',sans-serif;font-weight:700;font-size:30px;color:var(--white)}
.nav{position:absolute;left:370px;top:24px;display:flex;gap:24px;font-size:14px;font-weight:700;color:var(--white)}
.nav .active{color:var(--green);border-bottom:2px solid var(--green);padding-bottom:4px}
.search{position:absolute;left:917px;top:19px;width:162px;height:28px;border-radius:14px;background:var(--white);font-size:11px;color:#aaa;padding:7px 10px}
.search svg{position:absolute;right:10px;top:8px}
.hero{top:102px;left:0;width:1200px;height:382px;background:linear-gradient(100deg,#e9e1c8 0%,#d8cfb4 35%,#b7aa8e 60%,#8a8f94 85%,#a9b3b8 100%)}
.hero h1{position:absolute;left:112px;top:90px;font-family:'Sofia',cursive;font-weight:400;font-size:64px;color:var(--ink)}
.hero p{position:absolute;left:112px;top:205px;font-family:'Sofia',cursive;font-size:36px;line-height:48px;color:var(--ink);text-align:center}
.sidebar{top:349px;left:1137px;width:50px;background:var(--white);box-shadow:0 0 4px rgba(0,0,0,.2)}
.sidebar .item{height:48px;display:flex;flex-direction:column;align-items:center;justify-content:center;font-size:8px;color:#333;border-bottom:1px solid #eee;text-align:center;line-height:10px}
.sidebar .dot{width:14px;height:14px;border-radius:50%;margin-bottom:3px}
.section-title{left:0;width:1200px;text-align:center;font-family:'Sofia',cursive;font-size:48px;color:var(--green)}
.dots{left:123px;width:954px;border-top:4px dotted var(--green)}
.about{left:125px;top:617px;width:950px;font-size:19px;line-height:27px}
.about p+p{margin-top:27px}
.grid{left:227px;display:flex;gap:4px}
.card{width:186px;text-align:center}
.card .photo{width:186px;height:186px;border:2px solid var(--green);background:radial-gradient(circle at 50% 55%,#c79a74 0,#9b5c36 45%,var(--wood) 100%)}
.card .name{margin-top:14px;font-size:12px;font-weight:700;color:#666}
.card .desc{font-size:12px;color:var(--muted)}
.card .price{margin-top:6px;font-size:12px;font-weight:700;color:var(--green)}
.person{text-align:center}
.person h3{font-size:32px;font-weight:700;color:var(--green);line-height:38px}
.person p{font-size:20px;line-height:27px;color:var(--text)}
.avatar{width:102px;height:102px;border-radius:50%;border:3px solid var(--green);background:linear-gradient(135deg,#b9c2b0,#6d7d6a)}
.chips{display:flex;justify-content:center;gap:14px;margin-top:8px;font-size:13px;color:var(--green);font-weight:700}
.chips span{display:flex;align-items:center;gap:5px}
.chips i{width:22px;height:22px;border-radius:50%;background:var(--green);display:inline-block}
.field{left:123px;width:952px;border:3px dotted var(--green);border-radius:10px;font-size:28px;color:#666;padding:14px 10px}
.btn{left:123px;top:2457px;width:196px;height:50px;border-radius:10px;background:var(--green);outline:3px dotted var(--green);outline-offset:2px;color:var(--white);font-size:21px;font-weight:900;text-align:center;line-height:50px}
.footer{left:0;top:2565px;width:1200px;height:318px;background:var(--green);color:var(--white)}
.scallop{left:0;top:2557px;width:1200px;height:16px;background:radial-gradient(circle at 10px 2px,var(--white) 8px,transparent 9px) 0 0/51px 16px repeat-x}
.social{left:125px;top:35px;display:flex;gap:15px}
.social i{width:26px;height:26px;border-radius:50%;border:2px solid var(--white);display:block}
.fcol{top:80px;font-size:13px;line-height:16px}
.fcol h4{font-size:16px;font-weight:700;margin-bottom:20px}
.fcol .row{display:flex;gap:8px;align-items:flex-start}
.fnav{left:0;top:257px;width:1200px;display:flex;justify-content:center;gap:24px;font-size:14px;font-weight:700}
.copy{left:0;top:292px;width:1200px;text-align:center;font-size:13px;font-weight:700}
</style>
</head>
<body>
<div class="page">

  <header class="abs topbar">
    <div class="links">Register &nbsp;&nbsp;/&nbsp;&nbsp; Login</div>
    <svg class="cart" width="24" height="22" viewBox="0 0 24 22" fill="none" stroke="#111" stroke-width="2"><path d="M1 2h4l3 12h12l2-9H6"/><circle cx="9" cy="19" r="1.6"/><circle cx="19" cy="19" r="1.6"/></svg>
  </header>

  <nav class="abs navbar">
    <div class="logo">Lovmira</div>
    <div class="nav">
      <span class="active">HOME</span><span>PRODUCTS</span><span>NEWS</span><span>ABOUT US</span><span>CONTACT US</span><span>SEND INQUIRY</span>
    </div>
    <div class="search">Please Enter Keyword
      <svg width="11" height="11" viewBox="0 0 11 11" fill="none" stroke="#111" stroke-width="2"><circle cx="4.5" cy="4.5" r="3.3"/><path d="M7 7l3 3"/></svg>
    </div>
  </nav>

  <section class="abs hero" role="img" aria-label="Banner photo of a smiling bride and groom in front of the Eiffel Tower">
    <h1>Wedding Day</h1>
    <p>A very delicasy and<br>connotion announcement</p>
  </section>

  <aside class="abs sidebar">
    <div class="item"><span class="dot" style="background:#1e7be0"></span>Customer<br>Service</div>
    <div class="item"><span class="dot" style="background:#3cb54a"></span>Chat</div>
    <div class="item"><span class="dot" style="background:#1fa3e0"></span>Call</div>
    <div class="item"><span class="dot" style="background:#36b02c"></span>Messenger</div>
    <div class="item">
      <svg width="14" height="14" viewBox="0 0 14 14" fill="#f08a1c"><circle cx="11" cy="3" r="2.2"/><circle cx="3" cy="7" r="2.2"/><circle cx="11" cy="11" r="2.2"/><path d="M3 7L11 3M3 7l8 4" stroke="#f08a1c" stroke-width="1.2"/></svg>Share</div>
    <div class="item">
      <svg width="16" height="14" viewBox="0 0 16 14"><rect x="1" y="1" width="14" height="10" rx="2" fill="#1e6fe0"/><circle cx="5" cy="6" r="1" fill="#fff"/><circle cx="8" cy="6" r="1" fill="#fff"/><circle cx="11" cy="6" r="1" fill="#fff"/></svg>Message</div>
    <div class="item" style="height:52px">
      <svg width="14" height="14" viewBox="0 0 14 14" fill="none" stroke="#333" stroke-width="1.5"><path d="M1 1h12M7 13V4M3 8l4-4 4 4"/></svg>Top</div>
  </aside>

  <h2 class="abs section-title" style="top:522px">Guangzhou Bluestone Stationery Co., Ltd.</h2>
  <div class="abs dots" style="top:597px"></div>
  <div class="abs about">
    <p>Our company is established in 2001, located in Guang Zhou, Guangdong Province.We are an professional manufacturer and exporter that is concerned with the design, development and production manufacturing wedding invitation card, favor boxes and other gift items.</p>
    <p>Our company products all passed the CE, FSC and BSCI accreditation. We are able to provide high-quality products to customers from around the world, main market areas include Europe(Germany, UK, France, Italy), USA, Asian(Japan, Korea, India), South America. We have always been the most trusted partner of our customers.</p>
  </div>

  <h2 class="abs section-title" style="top:858px">New Products</h2>
  <div class="abs dots" style="top:925px"></div>

  <div class="abs grid" style="top:953px">
    <div class="card"><div class="photo" role="img" aria-label="Burgundy laser cut invitation with kraft envelope on wood"></div><div class="name">PRODUCT 1</div><div class="desc">Vintage wedding invitation</div><div class="price">US $ 0,81 - US $ 1.17</div></div>
    <div class="card"><div class="photo" role="img" aria-label="Gold butterfly laser cut invitation on wood"></div><div class="name">PRODUCT 2</div><div class="desc">Vintage wedding invitation</div><div class="price">US $ 0,81 - US $ 1.17</div></div>
    <div class="card"><div class="photo" role="img" aria-label="Navy lace invitation with kraft envelope on wood"></div><div class="name">PRODUCT 3</div><div class="desc">Vintage wedding invitation</div><div class="price">US $ 0,81 - US $ 1.17</div></div>
    <div class="card"><div class="photo" role="img" aria-label="Gold lace pocket invitation on wood"></div><div class="name">PRODUCT 4</div><div class="desc">Vintage wedding invitation</div><div class="price">US $ 0,81 - US $ 1.17</div></div>
  </div>
  <div class="abs grid" style="top:1232px">
    <div class="card"><div class="photo" role="img" aria-label="Burgundy laser cut invitation with kraft envelope on wood"></div><div class="name">PRODUCT 5</div><div class="desc">Vintage wedding invitation</div><div class="price">US $ 0,81 - US $ 1.17</div></div>
    <div class="card"><div class="photo" role="img" aria-label="Gold butterfly laser cut invitation on wood"></div><div class="name">PRODUCT 6</div><div class="desc">Vintage wedding invitation</div><div class="price">US $ 0,81 - US $ 1.17</div></div>
    <div class="card"><div class="photo" role="img" aria-label="Navy lace invitation with kraft envelope on wood"></div><div class="name">PRODUCT 7</div><div class="desc">Vintage wedding invitation</div><div class="price">US $ 0,81 - US $ 1.17</div></div>
    <div class="card"><div class="photo" role="img" aria-label="Gold lace pocket invitation on wood"></div><div class="name">PRODUCT 8</div><div class="desc">Vintage wedding invitation</div><div class="price">US $ 0,81 - US $ 1.17</div></div>
  </div>

  <h2 class="abs section-title" style="top:1522px">Contact Us</h2>
  <div class="abs dots" style="top:1590px"></div>

  <div class="abs avatar" style="left:125px;top:1637px" role="img" aria-label="Staff portrait"></div>
  <div class="abs person" style="left:232px;top:1618px;width:320px"><h3>Marcus</h3><p>E-mail: marcus@bluestonecraft.com<br>Mobile phone: +86 13600421758<br>TEL: +86 13600421758</p></div>

  <div class="abs avatar" style="left:670px;top:1637px" role="img" aria-label="Staff portrait"></div>
  <div class="abs person" style="left:771px;top:1620px;width:320px"><h3>Elena</h3><p>E-mail: elena@bluestonecraft.com<br>TEL: +86 18200317425</p></div>

  <div class="abs avatar" style="left:125px;top:1788px" role="img" aria-label="Staff portrait"></div>
  <div class="abs person" style="left:232px;top:1770px;width:320px"><h3>Clara</h3><p>E-mail: clara@bluestonecraft.com<br>TEL: +86 18800463519</p>
    <div class="chips"><span><i></i>Messenger</span><span><i></i>Call</span></div></div>

  <div class="abs avatar" style="left:670px;top:1788px" role="img" aria-label="Staff portrait"></div>
  <div class="abs person" style="left:771px;top:1770px;width:320px"><h3>Sophie</h3><p>E-mail: sophie@bluestonecraft.com<br>Mobile phone: +86 02061457390<br>TEL: +86 18700529634</p>
    <div class="chips"><span><i></i>Messenger</span><span><i></i>Call</span></div></div>

  <div class="abs avatar" style="left:125px;top:1936px" role="img" aria-label="Staff portrait"></div>
  <div class="abs person" style="left:226px;top:1930px;width:320px"><h3>Grace</h3><p>E-mail: grace@stoneblue-cards.com<br>TEL: +86 18200317425</p></div>

  <h2 class="abs section-title" style="top:2072px">Send Message</h2>
  <div class="abs field" style="top:2157px;height:66px">*Email</div>
  <div class="abs field" style="top:2258px;height:172px">*Message Content</div>
  <div class="abs btn">SEND MESSAGE</div>

  <footer class="abs footer">
    <div class="abs social"><i></i><i></i><i></i></div>
    <div class="abs fcol" style="left:125px">
      <h4 style="margin-left:28px">Address</h4>
      <div class="row"><svg width="20" height="24" viewBox="0 0 20 24" fill="none" stroke="#fff" stroke-width="1.8"><path d="M10 23s8-8 8-13a8 8 0 0 0-16 0c0 5 8 13 8 13z"/><circle cx="10" cy="10" r="3"/></svg>
        <span>Rm B112, 3rd Floor,<br>Lanting Building,<br>Meihua Road, Guangzhou,<br>P.R. CHINA, 510420</span></div>
    </div>
    <div class="abs fcol" style="left:372px">
      <h4 style="margin-left:31px">Telephone</h4>
      <div class="row"><svg width="24" height="24" viewBox="0 0 24 24" fill="none" stroke="#fff" stroke-width="1.8"><path d="M4 3l4 1 2 5-3 2a12 12 0 0 0 6 6l2-3 5 2 1 4c-9 1-18-8-17-17z"/></svg>
        <span>+86 13600421758<br>+86 18700529634<br>+86 18800463519<br>18200317425<br>+86 18200317425</span></div>
    </div>
    <div class="abs fcol" style="left:634px">
      <h4 style="margin-left:25px">Mobile phone</h4>
      <div class="row"><svg width="18" height="26" viewBox="0 0 18 26" fill="none" stroke="#fff" stroke-width="1.8"><rect x="2" y="1" width="14" height="24" rx="2"/><path d="M7 21h4"/></svg>
        <span>+86 13600421758<br>+86 02061457390</span></div>
    </div>
    <div class="abs fcol" style="left:880px">
      <h4 style="margin-left:33px">E-mail</h4>
      <div class="row"><svg width="26" height="20" viewBox="0 0 26 20" fill="none" stroke="#fff" stroke-width="1.8"><rect x="1" y="1" width="24" height="18" rx="2"/><path d="M1 2l12 9 12-9"/></svg>
        <span>admin@bluestonecraft.com<br>elena@bluestonecraft.com<br>clara@bluestonecraft.com<br>sophie@bluestonecraft.com<br>grace@stoneblue-cards.com</span></div>
    </div>
    <div class="abs fnav"><span>HOME</span><span>PRODUCTS</span><span>NEWS</span><span>ABOUT US</span><span>CONTACT US</span><span>SEND INQUIRY</span><span>SITEMAP</span></div>
    <div class="abs copy">2022 Guangzhou Bluestone Stationery Co., ltd. (203502) All rights reserved</div>
  </footer>
  <div class="abs scallop"></div>

</div>
</body>
</html>
```